Belmora Wines

Hi all,

My name’s Tom Welling and I run a small wine brand based in the Canberra Wine District, Australia. I’m currently in the process of branding the business and am looking for a designer to help develop a new visual direction.

Background
I’ll be growing my own fruit from a leased vineyard site Named 'Ashbrook' and my family’s property named 'Tallin Park', with a stronger emphasis on organic practices and site expression.

The Direction
The brand will centre around single vineyard wines, with each wine reflecting the unique site it comes from. I’d like the branding to support this idea of place, origin, and authenticity.

In terms of visual style, I’m drawn to something that is:

Simple and effective
A balance between traditional and modern
Clean, considered, and not overly decorative

Nothing too over-the-top, the goal is something timeless that lets the wine and vineyard story speak for itself.

At this stage, I’m mainly looking for:

Conceptual design direction / ideas
Label design (with potential to expand into broader branding)

I’m open to creative interpretation, so if the story resonates with you, I’d love to see how you would approach it.

Below I've attached an example of the bottle shape I will be using.

Cheers,
Tom

Colors
0054AA
0677BA
7BADD7
CADEEF
E8F1F8
FFC000
F8CF3A
FAE287
FDF2CF
FEFAEE

Requirements
Must have
• Mix of modern and traditional

```html
<!DOCTYPE html>
<html lang="en">
<head>
<meta charset="utf-8">
<title>Belmora Vineyards – Tallin Park Shiraz Label</title>
<link rel="stylesheet" href="https://fonts.googleapis.com/css2?family=Cormorant+Garamond:wght@400;500&family=Mrs+Saint+Delafield&display=swap">
<style>
  :root {
    --canvas-bg: #e8f1f8;
    --paper: #fefaee;
    --ink: #2b2b2b;
    --ink-soft: #474747;
    --accent-blue: #0054aa;
    --mid-blue: #0677ba;
    --light-blue: #7badd7;
    --pale-blue: #cadeef;
    --gold: #ffc000;
    --gold-soft: #f8cf3a;
  }
  * { margin: 0; padding: 0; box-sizing: border-box; }
  html, body {
    width: 1200px;
    height: 1200px;
    overflow: hidden;
    background: var(--canvas-bg);
  }
  .canvas {
    width: 1200px;
    height: 1200px;
    display: flex;
    align-items: center;
    justify-content: center;
  }
  .label {
    position: relative;
    width: 780px;
    height: 1088px;
    background: var(--paper);
    box-shadow: 0 2px 14px rgba(0, 40, 90, 0.10);
    font-family: "Cormorant Garamond", Georgia, serif;
    color: var(--ink);
  }
  .brand {
    position: absolute;
    left: 275px;
    top: 112px;
  }
  .brand-name {
    display: block;
    font-size: 48px;
    font-weight: 500;
    line-height: 1;
    letter-spacing: 1.5px;
    color: var(--ink);
    padding-bottom: 6px;
    border-bottom: 1.5px solid var(--ink-soft);
  }
  .brand-sub {
    display: block;
    font-size: 29px;
    font-weight: 500;
    line-height: 1;
    letter-spacing: 1.5px;
    margin-top: 8px;
    color: var(--ink-soft);
  }
  .bird-emblem {
    position: absolute;
    left: 0;
    top: 321px;
    width: 236px;
    height: 444px;
    background: radial-gradient(ellipse at 45% 45%, var(--mid-blue) 0%, var(--mid-blue) 35%, var(--light-blue) 75%, var(--pale-blue) 100%);
    border-bottom: 6px solid var(--gold);
  }
  .vineyard-name {
    position: absolute;
    left: 275px;
    top: 420px;
    font-size: 54px;
    font-weight: 400;
    line-height: 1;
    color: var(--ink);
  }
  .variety {
    position: absolute;
    left: 272px;
    top: 478px;
    font-family: "Mrs Saint Delafield", cursive;
    font-size: 84px;
    line-height: 1;
    color: var(--accent-blue);
  }
  .origin {
    position: absolute;
    left: 275px;
    top: 640px;
    font-size: 21px;
    font-weight: 500;
    line-height: 1;
    letter-spacing: 0.3px;
    color: var(--ink-soft);
  }
  .vintage {
    position: absolute;
    left: 275px;
    top: 680px;
    font-size: 38px;
    font-weight: 500;
    line-height: 1;
    letter-spacing: 2px;
    color: var(--ink);
  }
  .specs {
    position: absolute;
    left: 275px;
    top: 736px;
    font-size: 23px;
    line-height: 1.5;
    color: var(--ink-soft);
  }
</style>
</head>
<body>
  <main class="canvas">
    <section class="label">
      <div class="brand">
        <span class="brand-name">BELMORA</span>
        <span class="brand-sub">VINEYARDS</span>
      </div>

      <div class="bird-emblem" role="img" aria-label="Watercolour illustration of a bird with spread wings shaped like a vine leaf"></div>

      <h1 class="vineyard-name">Tallin Park</h1>
      <p class="variety">Shiraz</p>
      <p class="origin">WINE OF ORIGIN, CANBERRA</p>
      <p class="vintage">2026</p>
      <p class="specs">13.5% vol.<br>75cl</p>
    </section>
  </main>
</body>
</html>
```